The Northmoor Aid League needs a graphic of their innovation approach

What we need?
- we have designed a new innovation approach (see attached). An innovation approach is the process one goes through in order to design and launch a new product or service.
- This new graphic will be used in meetings to help others understand what innovation is and how we do it. It will also be used in training sessions and be the starting point for innovation training materials we are creating
- We have created this draft graphic by copying and pasting new words over another charities innovation process
- We would like you to use your design magic and create our very own innovation process graphic. We would like it to be neat, simple, non fussy, easy to understand /read and in line with our brand colours
Attached:
1. PowerPoint:
- Slide 1: our innovation process
- Slide 2 explanation of process to bring it to life
- Slide 3&4: brand colours
- Slide 5: inspiration / examples of other processes we like the look of
2. Typeface brand guidelines
We can't wait to see what you come up with! Thank you :)
internal employees
Charity

```html
<!DOCTYPE html>
<html lang="en">
<head>
<meta charset="utf-8">
<title>Innovation Approach – The Northmoor Aid League</title>
<link rel="stylesheet" href="https://fonts.googleapis.com/css2?family=Source+Sans+3:wght@600;700&display=swap">
<style>
  :root {
    --blue: #1a8fc3;
    --red: #e3211b;
    --yellow: #f6b53c;
    --navy: #1b2b4b;
    --shadow-grey: #dddddc;
    --disc-light: #f4f4f4;
    --disc-dark: #e1e1e1;
    --paper: #ffffff;
  }
  html, body {
    margin: 0;
    padding: 0;
    width: 1200px;
    height: 999px;
    overflow: hidden;
    background: var(--paper);
  }
  .process-graphic {
    display: block;
    width: 1200px;
    height: 999px;
    font-family: "Source Sans 3", "Source Sans Pro", sans-serif;
  }
  .backdrop-disc { fill: var(--shadow-grey); }
  .stage-ring { fill: var(--paper); }
  .stage-disc { fill: url(#discShade); }
  .ribbon { fill: none; stroke-width: 25; stroke-linecap: butt; }
  .ribbon--blue { stroke: var(--blue); }
  .ribbon--red { stroke: var(--red); }
  .ribbon--yellow { stroke: var(--yellow); }
  .cap--blue { fill: var(--blue); }
  .cap--yellow { fill: var(--yellow); }
  .stage-title {
    fill: var(--navy);
    font-size: 19px;
    font-weight: 700;
    text-anchor: middle;
    letter-spacing: 0.2px;
  }
  .step-label {
    font-size: 17px;
    font-weight: 600;
    letter-spacing: 1.6px;
  }
  .step-label--blue { fill: var(--blue); }
  .step-label--red { fill: var(--red); }
  .step-label--yellow { fill: var(--yellow); }
  .icon-fill { fill: var(--navy); }
  .icon-line { fill: none; stroke: var(--navy); stroke-width: 2; stroke-linecap: round; }
  .icon-placeholder { fill: var(--navy); opacity: 0.85; }
</style>
</head>
<body>
<svg class="process-graphic" viewBox="0 0 1200 999" xmlns="http://www.w3.org/2000/svg" role="img" aria-label="The Northmoor Aid League innovation approach: Challenge, Opportunity Statement, Concepts, Solution, Launch">
  <defs>
    <radialGradient id="discShade" cx="50%" cy="35%" r="65%">
      <stop offset="0%" stop-color="var(--disc-light)"/>
      <stop offset="100%" stop-color="var(--disc-dark)"/>
    </radialGradient>
    <path id="arc-insight" d="M268.9,639 A133,133 0 0 0 417,553.5"/>
    <path id="arc-test" d="M565.9,639 A133,133 0 0 0 708.5,566.3"/>
    <path id="arc-ideate" d="M322.5,319.2 A125,125 0 0 1 494.8,249.6"/>
    <path id="arc-validate" d="M397.2,244.5 A125,125 0 0 1 564.7,353.3"/>
    <path id="arc-delivery" d="M738,237 A125,125 0 0 1 856.9,400.6"/>
  </defs>

  <!-- soft backdrop discs -->
  <g class="backdrops">
    <circle class="backdrop-disc" cx="292" cy="508" r="118"/>
    <circle class="backdrop-disc" cx="440" cy="362" r="118"/>
    <circle class="backdrop-disc" cx="589" cy="508" r="118"/>
    <circle class="backdrop-disc" cx="738" cy="362" r="118"/>
    <circle class="backdrop-disc" cx="887" cy="508" r="118"/>
  </g>

  <!-- stage discs -->
  <g class="stages">
    <circle class="stage-ring" cx="292" cy="508" r="92"/><circle class="stage-disc" cx="292" cy="508" r="79"/>
    <circle class="stage-ring" cx="440" cy="362" r="92"/><circle class="stage-disc" cx="440" cy="362" r="79"/>
    <circle class="stage-ring" cx="589" cy="508" r="92"/><circle class="stage-disc" cx="589" cy="508" r="79"/>
    <circle class="stage-ring" cx="738" cy="362" r="92"/><circle class="stage-disc" cx="738" cy="362" r="79"/>
    <circle class="stage-ring" cx="887" cy="508" r="92"/><circle class="stage-disc" cx="887" cy="508" r="79"/>
  </g>

  <!-- flowing ribbon -->
  <g class="ribbons">
    <path class="ribbon ribbon--blue" d="M52,432 H185 C200,432 208,440 204.5,452 A105,105 0 1 0 366,435 A105,105 0 0 1 440,257"/>
    <circle class="cap--blue" cx="52" cy="432" r="12.5"/>
    <path class="ribbon ribbon--red" d="M440,257 A105,105 0 0 1 514.5,435 A105,105 0 1 0 663.5,435 A105,105 0 0 1 738,257"/>
    <path class="ribbon ribbon--yellow" d="M738,257 A105,105 0 0 1 812.5,435 A105,105 0 1 0 974.5,452 C971,440 979,432 994,432 H1128"/>
    <circle class="cap--yellow" cx="1128" cy="432" r="12.5"/>
  </g>

  <!-- step labels along the ribbon -->
  <g class="step-labels">
    <text class="step-label step-label--blue"><textPath href="#arc-insight" startOffset="50%" text-anchor="middle">INSIGHT</textPath></text>
    <text class="step-label step-label--red"><textPath href="#arc-test" startOffset="50%" text-anchor="middle">TEST</textPath></text>
    <text class="step-label step-label--blue"><textPath href="#arc-ideate" startOffset="50%" text-anchor="middle">IDEATE</textPath></text>
    <text class="step-label step-label--red"><textPath href="#arc-validate" startOffset="50%" text-anchor="middle">(IN)VALIDATE</textPath></text>
    <text class="step-label step-label--yellow"><textPath href="#arc-delivery" startOffset="50%" text-anchor="middle">DELIVERY PLAN</textPath></text>
  </g>

  <!-- stage: challenge -->
  <g class="stage stage--challenge">
    <g class="icon icon--mountain">
      <polygon class="icon-fill" points="254,510 278,474 288,488 296,462 322,510"/>
      <polygon class="icon-fill" points="305,510 316,490 332,510"/>
      <line class="icon-line" x1="296" y1="462" x2="296" y2="445"/>
      <polygon class="icon-fill" points="296,445 306,449 296,453"/>
    </g>
    <text class="stage-title" x="292" y="541">CHALLENGE</text>
  </g>

  <!-- stage: opportunity statement -->
  <g class="stage stage--opportunity">
    <circle class="icon-placeholder" cx="440" cy="331" r="20" role="img" aria-label="Icon: person surrounded by outward arrows"/>
    <text class="stage-title" x="440" y="388">OPPORTUNITY</text>
    <text class="stage-title" x="440" y="408">STATEMENT</text>
  </g>

  <!-- stage: concepts -->
  <g class="stage stage--concepts">
    <circle class="icon-placeholder" cx="589" cy="474" r="24" role="img" aria-label="Icon: head in profile with turning gears"/>
    <text class="stage-title" x="589" y="541">CONCEPTS</text>
  </g>

  <!-- stage: solution -->
  <g class="stage stage--solution">
    <g class="icon icon--bulb">
      <path class="icon-line" d="M732,352 C728,344 724,339 724,331 A14,14 0 1 1 752,331 C752,339 748,344 744,352 Z"/>
      <rect class="icon-fill" x="732" y="353" width="12" height="11" rx="2"/>
      <line class="icon-line" x1="738" y1="302" x2="738" y2="309"/>
      <line class="icon-line" x1="722" y1="307" x2="725" y2="313"/>
      <line class="icon-line" x1="754" y1="307" x2="751" y2="313"/>
      <line class="icon-line" x1="712" y1="318" x2="718" y2="321"/>
      <line class="icon-line" x1="764" y1="318" x2="758" y2="321"/>
    </g>
    <text class="stage-title" x="738" y="398">SOLUTION</text>
  </g>

  <!-- stage: launch -->
  <g class="stage stage--launch">
    <g class="icon icon--rocket">
      <path class="icon-fill" d="M923,455 C905,456 888,466 877,482 L868,483 L854,496 L867,497 L874,504 L875,517 L888,503 L889,494 C905,483 915,466 923,455 Z"/>
      <circle cx="903" cy="468" r="4.5" fill="var(--disc-light)"/>
      <path class="icon-fill" d="M866,500 C860,502 856,507 853,512 C858,510 864,508 868,503 Z"/>
    </g>
    <text class="stage-title" x="887" y="541">LAUNCH</text>
  </g>
</svg>
</body>
</html>
```